Commercial Real Estate Company Needs Website Redesign

Velmarco is a commercial real estate firm that is based in San Diego, but has offices and properties across the U.S. The current website was completed almost 3 years ago and is need of a refresh. We will rework the existing Wordpress CMS system, but require a new design. We have a great programmer who can take the design into wordpress. I need a design template for each page types, There are are approximately 20 pages for each section of our site. There are 4 Sections: Corporate, Hospitality, Commercial/Residential, and Receiver/Bankruptcy. See attached creative brief for the initial pages we would like drafted.

Industry/Entity Type

Real Estate

```html
<!DOCTYPE html>
<html lang="en">
<head>
<meta charset="utf-8">
<title>Velmarco Hospitality</title>
<link href="https://fonts.googleapis.com/css2?family=Oswald:wght@400;500&family=Arimo:wght@400;700&display=swap" rel="stylesheet">
<style>
:root{
  --navy:#13243f;
  --navy-deep:#0e1c33;
  --menu:#142744;
  --orange:#f5a42c;
  --page:#f2f2f2;
  --ink:#333a44;
  --muted:#a9adb3;
  --rule:#b9bcc1;
  --soft-rule:#e1e2e4;
  --white:#ffffff;
  --foot-text:#9aa6b8;
}
*{margin:0;padding:0;box-sizing:border-box}
html,body{width:1200px;height:2222px;overflow:hidden}
body{position:relative;background:var(--page);font-family:"Arimo",Arial,sans-serif;color:var(--ink)}
.abs{position:absolute}
.site-header{left:0;top:0;width:1200px;height:111px;background:var(--navy)}
.brand{left:99px;top:24px;display:flex;align-items:center;gap:14px;font-family:"Oswald",sans-serif;font-weight:500;font-size:44px;letter-spacing:2px;color:var(--white);line-height:1}
.brand-mark{width:34px;height:34px;background:var(--orange)}
.call{right:256px;top:22px;font-family:"Oswald",sans-serif;font-size:22px;line-height:30px;color:var(--orange);white-space:nowrap;text-align:right}
.social{left:962px;top:16px;display:flex;gap:10px}
.social span{width:40px;height:40px;border-radius:50%;background:#5d6a7e;display:block}
.main-nav{right:99px;top:72px;display:flex;gap:10px;font-size:17px;color:var(--white)}
.main-nav .sep{color:#8391a6}
.side-menu{left:99px;top:131px;width:229px;height:400px;background:var(--menu);border:2px solid #0b1628;padding:38px 0 0 50px;list-style:none}
.side-menu li{font-size:17px;color:#8c9ab0;height:50px}
.side-menu li.active{color:var(--white)}
.hero{left:341px;top:131px;width:760px;height:400px;border:4px solid var(--white);background:linear-gradient(160deg,#1c3c7a 0%,#3b66b0 35%,#d9c7a3 60%,#6a5238 100%)}
.section-title{font-family:"Oswald",sans-serif;font-weight:500;color:var(--orange);text-transform:uppercase;line-height:1}
.welcome-title{left:0;width:1200px;top:568px;text-align:center;font-size:29px}
.welcome-sub{left:0;width:1200px;top:618px;text-align:center;font-size:19px;font-weight:700;color:#666c75;letter-spacing:.5px}
.lede{left:310px;width:580px;top:652px;text-align:center;font-size:14px;line-height:17px;color:var(--muted)}
.read-more{display:flex;align-items:center;gap:14px;font-size:13px;color:#444a52;text-transform:uppercase}
.read-more::before,.read-more::after{content:"";flex:1;height:1px;background:var(--rule)}
.welcome-more{left:304px;width:592px;top:727px}
.divider{left:99px;width:1002px;height:1px;background:var(--soft-rule)}
.service{top:822px;width:330px;text-align:center}
.service .photo{width:276px;height:276px;margin:0 auto;border-radius:50%;border:11px solid #e4e4e4;box-shadow:0 0 0 1px #d2d2d2}
.service h2{margin-top:46px;font-size:31px}
.service p{margin:14px auto 0;width:300px;font-size:15px;line-height:19px;color:var(--muted)}
.service .read-more{width:250px;margin:18px auto 0}
.fid-title{left:99px;top:1338px;font-size:36px}
.news-title{left:768px;top:1338px;font-size:36px}
.card-photo{border:5px solid var(--white);box-shadow:0 0 0 1px #d9d9d9}
.fid-item{left:99px;width:568px;height:220px}
.fid-item .card-photo{position:absolute;left:2px;top:0;width:321px;height:213px}
.fid-text{position:absolute;left:353px;top:0;width:210px}
.item-head{font-size:15px;color:#444a52;text-transform:uppercase;letter-spacing:.3px}
.fid-text p{margin-top:6px;font-size:13.5px;line-height:18px;color:var(--muted)}
.fid-text .read-more{margin-top:12px}
.vrule{left:704px;top:1335px;width:1px;height:560px;background:var(--soft-rule)}
.news-item{left:768px;width:333px}
.news-item .card-photo{width:333px;height:155px}
.news-item .item-head{margin-top:16px}
.news-item p{margin-top:6px;font-size:13.5px;line-height:18px;color:var(--muted)}
.news-rule{left:768px;top:1636px;width:333px;height:1px;background:var(--soft-rule)}
.site-footer{left:0;top:1926px;width:1200px;height:234px;background:var(--navy)}
.foot-bar{left:0;top:2160px;width:1200px;height:62px;background:var(--navy-deep);border-top:1px solid #1d3152}
.foot-title{font-family:"Oswald",sans-serif;font-weight:500;font-size:25px;color:var(--white);text-transform:uppercase}
.foot-col{top:1962px}
.email{left:119px;top:2017px;width:293px;height:45px;background:var(--white);border-radius:3px;padding:0 15px;font-size:16px;line-height:45px;color:#222}
.subscribe{left:119px;top:2081px;width:293px;height:45px;background:var(--white);border-radius:3px;text-align:center;font-size:17px;line-height:45px;color:#222}
.foot-vr{top:1966px;width:1px;height:163px;background:#4a5a74}
.foot-list{list-style:none;margin-top:18px}
.foot-list li{font-size:15px;line-height:35px;color:var(--foot-text);white-space:nowrap}
.copyright{left:119px;top:2182px;font-size:14px;color:#aab3c1}
</style>
</head>
<body>
<header class="site-header abs">
  <div class="brand abs"><span class="brand-mark"></span>VELMARCO</div>
  <div class="call abs">Call : 555 - 310 - 4870</div>
  <div class="social abs" aria-label="Social links"><span></span><span></span><span></span></div>
  <nav class="main-nav abs">
    <span>Who we are</span><span class="sep">/</span>
    <span>What we do</span><span class="sep">/</span>
    <span>What we’ve done</span><span class="sep">/</span>
    <span>Contact Us</span><span class="sep">/</span>
    <span>Velmarco Home</span>
  </nav>
</header>

<ul class="side-menu abs">
  <li class="active">Home</li>
  <li>About Us</li>
  <li>Team</li>
  <li>News</li>
  <li>Corporate Culture</li>
  <li>Join Our Team</li>
  <li>Resources</li>
</ul>
<div class="hero abs" role="img" aria-label="Modern resort villa with palm tree and lit pool at dusk"></div>

<h1 class="section-title welcome-title abs">Welcome Velmarco</h1>
<div class="welcome-sub abs">COMFORTABLE HOTEL OF YOUR DREAMS</div>
<p class="lede abs">Lorem ipsum dolor sit amet, consectetur adipiscing elit, sed do eiusmod tempor incididunt ut labore et dolore magna aliqua Ut enim ad minim veniam, quis nostrud exercitation ullamco laboris nisi ut aliquip</p>
<div class="read-more welcome-more abs">Read More</div>
<div class="divider abs" style="top:785px"></div>

<section class="service abs" style="left:70px">
  <div class="photo" role="img" aria-label="High-rise hotel tower beside a pool" style="background:linear-gradient(180deg,#6fa6dc 0%,#d8c6a8 55%,#2f9fc7 85%)"></div>
  <h2 class="section-title">Commercial</h2>
  <p>Lorem ipsum dolor sit amet, consectetur adipiscing elit, sed do eiusmod tempor incididunt ut labore et dolore</p>
  <div class="read-more">Read More</div>
</section>
<section class="service abs" style="left:435px">
  <div class="photo" role="img" aria-label="Hotel bedroom with purple bedding" style="background:linear-gradient(180deg,#8c7f86 0%,#6b5a70 45%,#b9a7c2 75%,#4a3e4a 100%)"></div>
  <h2 class="section-title">Residential</h2>
  <p>Lorem ipsum dolor sit amet, consectetur adipiscing elit, sed do eiusmod tempor incididunt ut labore et dolore</p>
  <div class="read-more">Read More</div>
</section>
<section class="service abs" style="left:790px">
  <div class="photo" role="img" aria-label="Business partners shaking hands" style="background:linear-gradient(180deg,#e7e2dc 0%,#bfb7ae 40%,#2f3338 75%,#1d2024 100%)"></div>
  <h2 class="section-title">Owners/Investors</h2>
  <p>Lorem ipsum dolor sit amet, consectetur adipiscing elit, sed do eiusmod tempor incididunt ut labore et dolore</p>
  <div class="read-more">Read More</div>
</section>
<div class="divider abs" style="top:1301px"></div>

<h2 class="section-title fid-title abs">Fiduciary Services</h2>
<article class="fid-item abs" style="top:1397px">
  <div class="card-photo" role="img" aria-label="Bright hotel suite with bed and desk" style="background:linear-gradient(135deg,#9d9890 0%,#e9e4dc 45%,#c9b8a0 80%,#7a6452 100%)"></div>
  <div class="fid-text">
    <div class="item-head">Lorem ipsum dolor sit</div>
    <p>Lorem ipsum dolor sit amet, consectetuer adipiscing elit, sed diam nonummy nibh euismod tincidunt ut laoreet dolore magna aliquam erat volutpat. Ut wisi enim ad minim veniam, quis nostrud exerci tation ullamcorper suscipit</p>
    <div class="read-more">Read More</div>
  </div>
</article>
<article class="fid-item abs" style="top:1657px">
  <div class="card-photo" role="img" aria-label="Hotel entrance lit at night" style="background:linear-gradient(160deg,#2c3a66 0%,#5a4a5c 40%,#c98a4a 70%,#3a2a22 100%)"></div>
  <div class="fid-text">
    <div class="item-head">Lorem ipsum dolor sit</div>
    <p>Lorem ipsum dolor sit amet, consectetuer adipiscing elit, sed diam nonummy nibh euismod tincidunt ut laoreet dolore magna aliquam erat volutpat. Ut wisi enim ad minim veniam, quis nostrud exerci tation ullamcorper suscipit</p>
    <div class="read-more">Read More</div>
  </div>
</article>
<div class="vrule abs"></div>

<h2 class="section-title news-title abs">Latest News</h2>
<article class="news-item abs" style="top:1397px">
  <div class="card-photo" role="img" aria-label="Waterfront terrace dining at dusk" style="background:linear-gradient(180deg,#3d5c8c 0%,#6a86aa 40%,#c08a48 70%,#3a2a1e 100%)"></div>
  <div class="item-head">Lorem ipsum dolor sit</div>
  <p>Lorem ipsum dolor sit amet, consectetuer adipiscing elit, sed diam nonummy nibh euismod tincidunt</p>
</article>
<div class="news-rule abs"></div>
<article class="news-item abs" style="top:1659px">
  <div class="card-photo" role="img" aria-label="Waterfront terrace dining at dusk" style="background:linear-gradient(180deg,#3d5c8c 0%,#6a86aa 40%,#c08a48 70%,#3a2a1e 100%)"></div>
  <div class="item-head">Lorem ipsum dolor sit</div>
  <p>Lorem ipsum dolor sit amet, consectetuer adipiscing elit, sed diam nonummy nibh euismod tincidunt</p>
</article>

<footer class="site-footer abs"></footer>
<div class="foot-col abs" style="left:119px"><div class="foot-title">Newsletter</div></div>
<div class="email abs">Enter your email</div>
<div class="subscribe abs">Subscribe</div>
<div class="foot-vr abs" style="left:481px"></div>
<div class="foot-col abs" style="left:548px">
  <div class="foot-title">Follow Us</div>
  <ul class="foot-list">
    <li>Friendlane</li><li>Chirpwire</li><li>Workcircle</li><li>Streamcast</li>
  </ul>
</div>
<div class="foot-vr abs" style="left:716px"></div>
<div class="foot-col abs" style="left:780px">
  <div class="foot-title">Contact Us</div>
  <ul class="foot-list">
    <li>Velmarco Hotels &amp; Resorts</li>
    <li>A Premier Hotel Management Company</li>
    <li>2418 Harbor Crest Way, Suite 210, Lakemont, CA</li>
    <li>92101 USA &nbsp;|&nbsp; Phone: 555-310-4870</li>
  </ul>
</div>
<div class="foot-bar abs"></div>
<div class="copyright abs">© 2014 Velmarco &nbsp;/&nbsp; All Rights Reserved</div>
</body>
</html>
```